Corwin Pinnacle Lighting Commercial & Residential Landscape Lighting

Hello, I am looking for an Ad Design that I can use to promote ads on Facebook and other social media platforms. I want this ad to be a split screen ad meaning one photo at the top and one photo at the bottom to include a southern style home without outdoor landscape lighting & then the same picture at the bottom with outdoor landscape lighting. Add text to the graphic that talks about the difference landscape lighting does to your home. I want this ad to look professional and have professional design elements to the ad. I also have a logo I have uploaded below. We specialize in commercial grade outdoor landscape lighting, custom flag poles, outdoor audio, and we are locally and veteran owned. We offer lifetime warranty and quarterly maintenance on products.

```html
<!DOCTYPE html>
<html lang="en">
<head>
<meta charset="utf-8">
<title>Corwin Pinnacle Lighting – Transform Your Place Ads</title>
<link href="https://fonts.googleapis.com/css2?family=Great+Vibes&family=Lato:ital,wght@1,900&family=Josefin+Sans:wght@400;600;700&family=Quicksand:wght@500&family=Oswald:wght@600&family=Jost:wght@500&display=swap" rel="stylesheet">
<style>
  :root {
    --backdrop: #1d1d1d;
    --ad-black: #0b0b0b;
    --ad-panel: #121212;
    --gold: #eba664;
    --gold-light: #f6d3a3;
    --gold-deep: #d58a47;
    --white: #f4f1ec;
    --wood-light: #dac5a5;
    --wood-dark: #a98a66;
  }
  * { box-sizing: border-box; margin: 0; padding: 0; }
  html, body { width: 1200px; height: 836px; overflow: hidden; }
  body {
    background: radial-gradient(ellipse at 50% 45%, #2a2a2a 0%, var(--backdrop) 70%);
    position: relative;
    font-family: "Quicksand", sans-serif;
  }
  .ad {
    position: absolute;
    top: 100px;
    width: 500px;
    height: 623px;
    background: var(--ad-black);
    overflow: hidden;
    box-shadow: 0 18px 30px rgba(0,0,0,.55);
  }
  .ad--classic { left: 74px; }
  .ad--estimate { left: 614px; }

  .ad__header {
    position: relative;
    background: linear-gradient(180deg, #151515 0%, var(--ad-black) 100%);
  }
  .ad--classic .ad__header { height: 107px; }
  .ad--estimate .ad__header { height: 136px; }

  .headline-script {
    font-family: "Great Vibes", cursive;
    color: var(--gold);
    font-size: 60px;
    line-height: 1;
    font-weight: 400;
  }
  .headline-bold {
    font-family: "Lato", sans-serif;
    font-style: italic;
    font-weight: 900;
    color: var(--gold-light);
  }
  .ad--classic .headline { position: absolute; left: 36px; top: 28px; white-space: nowrap; }
  .ad--classic .headline-bold { font-size: 36px; letter-spacing: -0.5px; margin-left: 4px; }
  .ad--estimate .headline { position: absolute; left: 28px; top: 26px; }
  .ad--estimate .headline-bold {
    display: block; font-size: 24px; margin: -6px 0 0 118px; letter-spacing: -0.3px;
  }

  .brand-name {
    position: absolute;
    font-family: "Josefin Sans", sans-serif;
    font-weight: 400;
    color: var(--gold);
    text-transform: uppercase;
    text-align: center;
    line-height: 1.15;
  }
  .ad--estimate .brand-name { left: 322px; top: 40px; width: 150px; font-size: 20px; letter-spacing: 1.5px; }
  .ad--classic .brand-name { left: 322px; top: 38px; width: 156px; font-size: 20px; letter-spacing: 1.5px; }

  .photo {
    position: relative;
    border-top: 2px solid var(--gold-deep);
  }
  .photo--before {
    background: linear-gradient(180deg, #5b6478 0%, #2c3038 40%, #1b1e1f 75%, #23281f 100%);
  }
  .photo--after {
    background:
      radial-gradient(ellipse at 50% 62%, rgba(240,180,90,.55) 0%, rgba(160,110,50,.25) 35%, transparent 65%),
      linear-gradient(180deg, #4a5570 0%, #2b2a2a 40%, #2a2214 75%, #2a3320 100%);
  }
  .ad--classic .photo--before { height: 167px; }
  .ad--classic .photo--after { height: 185px; }
  .ad--estimate .photo--before { height: 166px; }
  .ad--estimate .photo--after { height: 184px; }

  .photo__label { position: absolute; text-transform: uppercase; line-height: 1.05; }
  .ad--classic .photo__label {
    left: 38px; bottom: 10px;
    font-family: "Lato", sans-serif; font-style: italic; font-weight: 900;
    font-size: 16px; color: var(--gold); letter-spacing: .5px;
  }
  .ad--estimate .photo__label {
    right: 25px; bottom: 18px; text-align: right;
    font-family: "Oswald", sans-serif; font-weight: 600;
    font-size: 21px; color: var(--gold); letter-spacing: .3px;
    text-shadow: 0 0 3px #000, 1px 1px 0 #000, -1px -1px 0 #000;
  }

  .ad__footer {
    position: relative;
    border-top: 2px solid var(--gold-deep);
    background: linear-gradient(180deg, #181818 0%, var(--ad-panel) 100%);
  }
  .ad--classic .ad__footer { height: 164px; }
  .ad--estimate .ad__footer { height: 137px; }

  .wood-band { position: absolute; left: 0; bottom: 0; width: 100%; height: 90px; }

  .tagline {
    position: absolute; left: 32px; top: 20px;
    font-family: "Josefin Sans", sans-serif; font-weight: 700;
    font-size: 25px; line-height: 1.1; color: var(--gold); letter-spacing: .8px;
    text-transform: uppercase;
  }
  .ad--classic .brand-name--footer { left: 322px; top: 46px; }

  .services { list-style: none; position: absolute; color: var(--white); }
  .services li { position: relative; padding-left: 20px; }
  .services li::before {
    content: ""; position: absolute; left: 2px; top: 50%;
    width: 4px; height: 4px; border-radius: 50%; background: var(--white);
  }
  .ad--classic .services { left: 34px; top: 84px; font-size: 15.5px; line-height: 17px; }
  .ad--estimate .services { left: 192px; top: 30px; font-size: 16.5px; line-height: 18.5px; }

  .offer { position: absolute; left: 36px; top: 24px; color: var(--gold); font-family: "Jost", sans-serif; font-weight: 500; }
  .offer__big { display: block; font-size: 60px; line-height: 1; letter-spacing: 2px; }
  .offer__small { display: block; font-size: 15px; letter-spacing: 4.3px; margin-top: -2px; }
</style>
</head>
<body>

<section class="ad ad--classic">
  <header class="ad__header">
    <h1 class="headline"><span class="headline-script">Transform</span><span class="headline-bold">Your Place</span></h1>
  </header>
  <div class="photo photo--before" role="img" aria-label="Southern style home with wraparound porch at dusk, without landscape lighting">
    <p class="photo__label">Before<br>Lighting</p>
  </div>
  <div class="photo photo--after" role="img" aria-label="The same southern style home at dusk with warm landscape lighting on porch, shrubs and trees">
    <p class="photo__label">After<br>Lighting</p>
  </div>
  <footer class="ad__footer">
    <svg class="wood-band" viewBox="0 0 500 90" preserveAspectRatio="none" role="img" aria-label="Light wood grain texture band">
      <defs>
        <linearGradient id="woodClassic" x1="0" y1="0" x2="1" y2="1">
          <stop offset="0" stop-color="#dac5a5"/>
          <stop offset="1" stop-color="#a98a66"/>
        </linearGradient>
      </defs>
      <path d="M0 74 C180 78 380 60 500 12 L500 90 L0 90 Z" fill="url(#woodClassic)"/>
      <path d="M0 74 C180 78 380 60 500 12" fill="none" stroke="#eba664" stroke-width="2"/>
    </svg>
    <h2 class="tagline">Illuminate<br>with confidence</h2>
    <ul class="services">
      <li>Landscaping Lighting</li>
      <li>Holiday Lighting</li>
      <li>Permanent Installation</li>
    </ul>
    <p class="brand-name brand-name--footer" style="top:38px">Corwin Pinnacle Lighting</p>
  </footer>
</section>

<section class="ad ad--estimate">
  <header class="ad__header">
    <h1 class="headline"><span class="headline-script">Transform</span><span class="headline-bold">YOUR PLACE</span></h1>
    <p class="brand-name">Corwin Pinnacle Lighting</p>
  </header>
  <div class="photo photo--before" role="img" aria-label="Southern style home with wraparound porch at dusk, without landscape lighting">
    <p class="photo__label">Before<br>Lighting</p>
  </div>
  <div class="photo photo--after" role="img" aria-label="The same southern style home at dusk with warm landscape lighting on porch, shrubs and trees">
    <p class="photo__label">After<br>Lighting</p>
  </div>
  <footer class="ad__footer">
    <svg class="wood-band" viewBox="0 0 500 90" preserveAspectRatio="none" role="img" aria-label="Light wood grain texture band">
      <defs>
        <linearGradient id="woodEstimate" x1="0" y1="0" x2="1" y2="1">
          <stop offset="0" stop-color="#dac5a5"/>
          <stop offset="1" stop-color="#a98a66"/>
        </linearGradient>
      </defs>
      <path d="M0 74 C180 78 380 60 500 12 L500 90 L0 90 Z" fill="url(#woodEstimate)"/>
      <path d="M0 74 C180 78 380 60 500 12" fill="none" stroke="#eba664" stroke-width="2"/>
    </svg>
    <p class="offer"><span class="offer__big">FREE</span><span class="offer__small">ESTIMATES</span></p>
    <ul class="services">
      <li>Landscaping Lighting</li>
      <li>Holiday Lighting</li>
      <li>Permanent Installation</li>
    </ul>
  </footer>
</section>

</body>
</html>
```